The dental corner of brindlewood web page

website for dental office
Already have domain, mostly information only with address, telephone and google map and hours of operation on top. mobile friendly. SEO a most.

Target Market(s)

Local families

Industry/Entity Type

Dental Clinic

Number of Pages Required

1 page

Font styles to use
Serif

Colors

Designer to choose colors to be used in the design.

Requirements
Must have
• SEO
• Information to find the location
• mobile friendly
• dr's. biography
• services offered
• contect to social media (google, facebook, and instagram)
• Se habla espaƱol
• All insurance accepted
• request an appointment form to notify us

```html
<!DOCTYPE html>
<html lang="en">
<head>
<meta charset="utf-8">
<title>The Dental Corner of Brindlewood</title>
<link rel="stylesheet" href="https://fonts.googleapis.com/css2?family=Vollkorn:wght@400;500;600&family=Open+Sans:wght@400;600&display=swap">
<style>
:root{
  --blue:#0b4ea2;
  --blue-dark:#093f85;
  --green:#8cc63f;
  --ink:#222;
  --muted:#666;
  --dark:#151515;
  --light:#f1f3f3;
  --line:#e4e6e8;
  --white:#fff;
}
*{box-sizing:border-box;margin:0;padding:0}
html,body{width:1200px;height:3035px;overflow:hidden}
body{position:relative;font-family:"Open Sans",Arial,sans-serif;color:var(--ink);background:var(--white)}
.abs{position:absolute}

.top-bar{left:0;top:0;width:1200px;height:28px;background:var(--dark);color:#fff;font-size:11px}
.top-bar .call{left:132px;top:7px;display:flex;align-items:center;gap:8px}
.top-bar .social{right:132px;top:8px;display:flex;gap:6px}
.top-bar .social span{width:11px;height:11px;border-radius:50%;background:#fff;display:block}

.site-header{left:0;top:28px;width:1200px;height:124px;background:var(--white)}
.brand{left:130px;top:40px;display:flex;align-items:center;gap:10px;font-family:"Vollkorn",Georgia,serif;font-size:17px;color:var(--blue);font-weight:500;width:200px;line-height:1.15}
.brand .mark{width:36px;height:36px;border-radius:50%;background:var(--green);flex:none}
.main-nav{left:508px;top:50px;font-family:"Vollkorn",Georgia,serif;font-size:16px;color:var(--ink)}
.main-nav a{color:inherit;text-decoration:none;position:absolute;white-space:nowrap}
.main-nav a.active::after{content:"";position:absolute;left:0;right:0;bottom:-10px;height:3px;background:var(--green)}

.hero-photo{left:0;top:152px;width:1200px;height:566px;background:linear-gradient(90deg,#e9ddd0 0%,#efe6dc 35%,#e4e2df 60%,#d9dcda 100%)}
.hero-title{left:597px;top:296px;font-family:"Vollkorn",Georgia,serif;font-size:38px;line-height:41px;color:var(--blue);font-weight:500}
.hero-text{left:599px;top:402px;width:430px;font-size:12.5px;line-height:20px;color:#555}
.btn{background:var(--blue);color:#fff;font-family:"Vollkorn",Georgia,serif;font-size:14px;display:flex;align-items:center;justify-content:center;text-decoration:none}
.hero-btn{left:599px;top:500px;width:99px;height:37px}

.about{left:0;top:718px;width:1200px;height:557px;background:linear-gradient(180deg,#fff 0%,var(--light) 100%)}
.feature{top:658px;width:206px;height:176px;background:var(--green);color:#fff;text-align:center;font-family:"Vollkorn",Georgia,serif;font-size:17px;line-height:19px;font-weight:500;box-shadow:0 6px 14px rgba(0,0,0,.12)}
.feature.is-highlight{background:var(--blue)}
.feature svg{display:block;margin:26px auto 14px}
.doctor-ring{left:198px;top:890px;width:324px;height:324px;border-radius:50%;border:7px solid var(--blue);background:#fff;padding:8px}
.doctor-photo{width:100%;height:100%;border-radius:50%;background:linear-gradient(160deg,#d7d2cb,#c9b8a8 55%,#e9eef0)}
.about-title{left:605px;top:904px;font-family:"Vollkorn",Georgia,serif;font-size:28px;font-weight:400;color:var(--blue)}
.about-text{left:607px;top:990px;width:460px;font-size:12.5px;line-height:20px;color:#555}
.about-btn{left:607px;top:1109px;width:97px;height:38px}

.divider{display:flex;align-items:center;gap:6px;width:150px;justify-content:center}
.divider i{display:block;height:1px;background:#aaa;flex:1}
.divider b{width:20px;height:20px;border:1px solid #999;border-radius:50%}

.section-title{font-family:"Vollkorn",Georgia,serif;font-size:28px;font-weight:400;color:var(--blue);width:1200px;text-align:center;left:0}
.services-text{left:0;top:1386px;width:1200px;text-align:center;font-size:12.5px;line-height:20px;color:#555}
.service-grid{left:202px;top:1459px;width:800px;height:267px;display:grid;grid-template-columns:247px 300px 253px;grid-template-rows:130px 137px}
.service-cell{display:flex;flex-direction:column;align-items:center;justify-content:flex-end;padding-bottom:32px;gap:14px;border-right:1px solid var(--line);border-bottom:1px solid var(--line);font-family:"Vollkorn",Georgia,serif;font-size:18px;color:var(--ink)}
.service-cell.is-highlight{background:var(--blue);color:#fff;border-color:var(--blue)}
.service-cell.last-col{border-right:none}
.service-cell.last-row{border-bottom:none}

.appointment{left:0;top:1785px;width:1200px;height:552px;background:linear-gradient(120deg,#2f86c8 0%,#48a7b5 45%,#79c07f 75%,#9bcb6a 100%)}
.appointment .section-title{color:#fff;top:60px}
.field{background:rgba(255,255,255,.35);border:1px solid rgba(255,255,255,.55);color:#fff;font-family:"Vollkorn",Georgia,serif;font-size:13px;padding:10px 14px}
.send-btn{left:550px;top:2240px;width:100px;height:38px}

.suppliers-title{top:2360px}
.supplier{top:2460px;font-family:"Vollkorn",Georgia,serif;font-size:22px;font-weight:600;color:#555;letter-spacing:.5px;display:flex;align-items:center;gap:8px;white-space:nowrap}
.supplier .sq{width:18px;height:18px;background:#555}

.map{left:0;top:2560px;width:1200px;height:435px;background:linear-gradient(135deg,#e8e6df 0%,#efeee9 45%,#e2e6e1 70%,#dfe3ea 100%)}
.map-zoom{left:1020px;top:2695px;width:48px;height:82px;background:#fff;box-shadow:0 1px 4px rgba(0,0,0,.3);font-size:26px;text-align:center;line-height:40px;color:#333}
.info-panel{left:132px;top:2560px;width:330px;height:435px;background:var(--green);color:#fff;padding:42px 28px}
.info-panel h3{font-family:"Vollkorn",Georgia,serif;font-weight:500;font-size:22px;margin-bottom:18px}
.hours{display:grid;grid-template-columns:145px auto;row-gap:8px;font-size:13px;margin-bottom:30px}
.contact-list{list-style:none;font-size:13px}
.contact-list li{display:flex;align-items:center;gap:14px;margin-bottom:14px}
.follow{display:flex;gap:10px;margin-top:4px}
.follow span{width:20px;height:20px;border-radius:50%;background:#fff;display:block}

.bottom-bar{left:0;top:2995px;width:1200px;height:40px;background:var(--dark);color:#fff;font-size:11px}
.bottom-bar .copy{left:132px;top:13px}
.bottom-bar .links{right:132px;top:13px;display:flex;gap:24px}
</style>
</head>
<body>

<div class="top-bar abs">
  <div class="call abs">
    <svg width="11" height="11" viewBox="0 0 24 24"><path fill="#fff" d="M6.6 10.8a15 15 0 0 0 6.6 6.6l2.2-2.2a1 1 0 0 1 1-.25 11.4 11.4 0 0 0 3.6.57 1 1 0 0 1 1 1V20a1 1 0 0 1-1 1A17 17 0 0 1 3 4a1 1 0 0 1 1-1h3.5a1 1 0 0 1 1 1c0 1.25.2 2.450.57 3.57a1 1 0 0 1-.25 1z"/></svg>
    <span><b>Call for Consultation</b>&nbsp; 0800 555 01 234</span>
  </div>
  <div class="social abs"><span></span><span></span><span></span><span></span></div>
</div>

<header class="site-header abs">
  <div class="brand abs"><span class="mark"></span><span>The Dental Corner of Brindlewood</span></div>
  <nav class="main-nav abs">
    <a class="active" style="left:0">Home</a>
    <a style="left:99px">About Dr</a>
    <a style="left:216px">Services &#8964;</a>
    <a style="left:362px">Appointment</a>
    <a style="left:508px">Contact</a>
  </nav>
</header>

<div class="hero-photo abs" role="img" aria-label="Smiling child hugging a teddy bear in a bright dental clinic"></div>
<h1 class="hero-title abs">Make Your Dental<br>Experience a Lot Brighter</h1>
<p class="hero-text abs">Lorem ipsum dolor sit amet, consectetur adipiscing elit, sed do eiusmod tempor incididunt ut labore et dolore magna aliqua. Ut enim ad minim veniam, quis nostrud exercitation ullamco laboris nisi ut aliquip ex ea commodo consequat.</p>
<a class="btn hero-btn abs">Read More</a>

<section class="about abs"></section>

<div class="feature abs" style="left:166px">
  <svg width="52" height="52" viewBox="0 0 52 52" fill="none" stroke="#fff" stroke-width="2"><rect x="8" y="6" width="30" height="38" rx="2"/><path d="M14 16h18M14 23h18M14 30h10"/><circle cx="38" cy="36" r="8"/><path d="M34 36l3 3 5-6"/></svg>
  Accepting<br>Insurance Cards
</div>
<div class="feature abs" style="left:386px">
  <svg width="52" height="52" viewBox="0 0 52 52" fill="none" stroke="#fff" stroke-width="2"><circle cx="26" cy="24" r="10"/><path d="M26 8v5M26 35v5M10 24h5M37 24h5M15 13l3 3M34 32l3 3M37 13l-3 3M18 32l-3 3"/><path d="M22 44h8"/></svg>
  Using Innovative<br>Technology
</div>
<div class="feature is-highlight abs" style="left:605px">
  <svg width="52" height="52" viewBox="0 0 52 52" fill="none" stroke="#fff" stroke-width="2"><path d="M16 8c-6 0-9 5-9 11 0 8 4 12 5 22 1 4 5 4 6 0l3-9c1-3 5-3 6 0l3 9c1 4 5 4 6 0 1-10 5-14 5-22 0-6-3-11-9-11-4 0-6 2-8 2s-4-2-8-2z"/><path d="M21 22l4 4 7-8"/></svg>
  Guarantee Success<br>of Treatments
</div>
<div class="feature abs" style="left:823px">
  <svg width="52" height="52" viewBox="0 0 52 52" fill="none" stroke="#fff" stroke-width="2"><rect x="6" y="10" width="40" height="28" rx="2"/><path d="M13 18h16M13 25h12"/><circle cx="36" cy="28" r="5"/><path d="M33 33l-2 9 5-3 5 3-2-9"/></svg>
  Certified Dentist<br>Doctors
</div>

<div class="doctor-ring abs"><div class="doctor-photo" role="img" aria-label="Portrait of the dentist in a white coat"></div></div>
<h2 class="about-title abs">About Dr.Halloway</h2>
<div class="divider abs" style="left:607px;top:948px"><i></i><b></b><i></i></div>
<p class="about-text abs">Lorem ipsum dolor sit amet, consectetur adipiscing elit, sed do eiusmod tempor incididunt ut labore et dolore magna aliqua. Ut enim ad minim veniam, quis nostrud exercitation ullamco laboris nisi ut aliquip ex ea commodo consequat. Duis aute</p>
<a class="btn about-btn abs">Read More</a>

<h2 class="section-title abs" style="top:1315px">Our Services</h2>
<div class="divider abs" style="left:525px;top:1360px"><i></i><b></b><i></i></div>
<p class="services-text abs">Lorem ipsum dolor sit amet, consectetur adipiscing elit, sed do eiusmod<br>tempor incididunt ut labore et dolore magna aliqua.</p>

<div class="service-grid abs">
  <div class="service-cell"><svg width="36" height="40" viewBox="0 0 36 40" fill="none" stroke="var(--blue)" stroke-width="2"><path d="M11 4C6 4 4 8 4 13c0 6 3 9 4 17 1 4 4 4 5 0l2-7c1-2 5-2 6 0l2 7c1 4 4 4 5 0 1-8 4-11 4-17 0-5-2-9-7-9-3 0-5 2-7 2s-4-2-7-2z"/><path d="M30 2v6M27 5h6"/></svg>Teeth Whitening</div>
  <div class="service-cell is-highlight"><svg width="40" height="40" viewBox="0 0 40 40" fill="none" stroke="#fff" stroke-width="2"><path d="M13 5C7 5 5 9 5 14c0 6 3 9 4 17 1 4 4 4 5 0l2-7c1-2 5-2 6 0l2 7c1 4 4 4 5 0 1-8 4-11 4-17 0-5-2-9-7-9-3 0-5 2-7 2s-4-2-7-2z"/><path d="M14 17c3 3 9 3 12 0"/></svg>Cosmetic Dentisry</div>
  <div class="service-cell last-col"><svg width="30" height="40" viewBox="0 0 30 40" fill="none" stroke="var(--blue)" stroke-width="2"><path d="M6 4h18l-2 8H8z"/><path d="M9 16h12M10 22h10M11 28h8M13 34h4"/></svg>Dental Implants</div>
  <div class="service-cell last-row"><svg width="36" height="40" viewBox="0 0 36 40" fill="none" stroke="var(--blue)" stroke-width="2"><path d="M11 4C6 4 4 8 4 13c0 6 3 9 4 17 1 4 4 4 5 0l2-7c1-2 5-2 6 0l2 7c1 4 4 4 5 0 1-8 4-11 4-17 0-5-2-9-7-9-3 0-5 2-7 2s-4-2-7-2z"/><path d="M14 14v10M22 14v10"/></svg>Root Canal Therapy</div>
  <div class="service-cell last-row"><svg width="36" height="40" viewBox="0 0 36 40" fill="none" stroke="var(--blue)" stroke-width="2"><path d="M11 4C6 4 4 8 4 13c0 6 3 9 4 17 1 4 4 4 5 0l2-7c1-2 5-2 6 0l2 7c1 4 4 4 5 0 1-8 4-11 4-17 0-5-2-9-7-9-3 0-5 2-7 2s-4-2-7-2z"/><path d="M18 11v8M14 15h8"/></svg>Smile Enhancement</div>
  <div class="service-cell last-row last-col"><svg width="40" height="40" viewBox="0 0 40 40" fill="none" stroke="var(--blue)" stroke-width="2"><path d="M11 4C6 4 4 8 4 13c0 6 3 9 4 17 1 4 4 4 5 0l2-7c1-2 5-2 6 0l2 7"/><circle cx="26" cy="22" r="7"/><path d="M31 27l6 7"/></svg>Routine Checkups</div>
</div>

<section class="appointment abs" role="img" aria-label="Patient smiling in a dental chair with a blue to green overlay">
  <h2 class="section-title abs">Online Appointment</h2>
  <div class="divider abs" style="left:525px;top:104px"><i style="background:#fff"></i><b style="border-color:#fff"></b><i style="background:#fff"></i></div>
</section>
<div class="field abs" style="left:421px;top:1936px;width:358px;height:41px">Name</div>
<div class="field abs" style="left:421px;top:1989px;width:358px;height:41px">Phone #</div>
<div class="field abs" style="left:421px;top:2040px;width:174px;height:44px">Date</div>
<div class="field abs" style="left:605px;top:2040px;width:174px;height:44px">Time</div>
<div class="field abs" style="left:421px;top:2094px;width:358px;height:116px">Message</div>
<a class="btn send-btn abs">Send</a>

<h2 class="section-title suppliers-title abs">Pharmacy Suppliers</h2>
<div class="divider abs" style="left:525px;top:2408px"><i></i><b></b><i></i></div>
<div class="supplier abs" style="left:184px"><span class="sq"></span>Pellworth Rx</div>
<div class="supplier abs" style="left:412px">Tamsel Supply</div>
<div class="supplier abs" style="left:660px">Quenby Pharma</div>
<div class="supplier abs" style="left:870px">Larkmoor Goods</div>

<div class="map abs" role="img" aria-label="Street map showing the clinic location"></div>
<div class="map-zoom abs">+<br>&minus;</div>
<aside class="info-panel abs">
  <h3>Working Hours</h3>
  <div class="hours"><span>Mon - Fri</span><span>9.00 am - 6 .00 pm</span><span>Sat - Sun</span><span>Closed</span></div>
  <h3>Contact Information</h3>
  <ul class="contact-list">
    <li><svg width="12" height="14" viewBox="0 0 24 28"><path fill="#fff" d="M12 0a10 10 0 0 0-10 10c0 8 10 18 10 18s10-10 10-18A10 10 0 0 0 12 0zm0 14a4 4 0 1 1 0-8 4 4 0 0 1 0 8z"/></svg>51 Alder Road, Brindlewood</li>
    <li><svg width="13" height="13" viewBox="0 0 24 24"><path fill="#fff" d="M6.6 10.8a15 15 0 0 0 6.6 6.6l2.2-2.2a1 1 0 0 1 1-.25 11.4 11.4 0 0 0 3.6.57 1 1 0 0 1 1 1V20a1 1 0 0 1-1 1A17 17 0 0 1 3 4a1 1 0 0 1 1-1h3.5a1 1 0 0 1 1 1c0 1.25.2 2.45.57 3.57a1 1 0 0 1-.25 1z"/></svg>+1 555 800 150</li>
    <li><svg width="13" height="10" viewBox="0 0 26 20"><path fill="#fff" d="M0 0h26v20H0z"/><path d="M2 3l11 9 11-9" stroke="#8cc63f" stroke-width="2" fill="none"/></svg>care@dentalcorner.com</li>
  </ul>
  <h3 style="margin-top:26px">Follow Us</h3>
  <div class="follow"><span></span><span></span><span></span><span></span></div>
</aside>

<footer class="bottom-bar abs">
  <div class="copy abs">&copy; Copyright by Brindlewood Dental Group . All Right Reserved &copy; 2018</div>
  <div class="links abs"><span>Privacy Policy</span><span>Terms of Use</span></div>
</footer>

</body>
</html>
```